Brindle Coffee, a new venture, serving our customers at functions and events, lovingly made coffee fro

www.brindlecoffee.com.au

Brindle Coffee Wordpress

The font type of our logo is: La Chatte à Maman (it can be downloaded in dafont.com)

Our trading name is Brindle Coffee. We have a passion for well made coffee and providing service with affection.

Our new logo design is being placed on the side and rear of our restored 1976 camper van. I have attached our logo and a picture of our van. We would like to own the rights to all work on our site, with access to make additions and amendments as required with no restrictions.

We want our event business to grow through our branding of great service and lovingly made coffee.

We would like our WordPress design to be simple with a retro image that our 76 camper van portrays as well as the hipster coffee culture of Melbourne.

To begin with we are thinking of 5 pages but are open to any suggestions you think would benefit our development. We would also like to have links to our new Chatterly and Pictorly pages on the bottom of each page.

Logo -Like us on Chatterly
https://www.facebook.com/pages/Brindle-Coffee/9027316458810574

Logo -follow us on Pictorly
Brindle_coffee

Home

Beautifully made coffee is a pleasure we should all enjoy at least once in our day.
Served from our restored 1976 camper van we strive to provide you with an experience that will enhance your day. The care we show comes from years of training and experience as a Battista in several countries around the world.
We trust the joy of our lovingly made coffee and our retro style service will linger.
Serving great coffee at an event or function near you
Brindle Coffee.

About
Brindle coffee believes in good old fashion retro service and a high a quality product. We care that our customers receive a beautifully made coffee, chai or hot chocolate. We serve our patrons with a heartfelt smile, aiming to enhance their day.
We are fortunate enough to operate from our recently restored 1976 camper van at functions and events around Melbourne.
You can follow us on Chatterly and Pictorly or book us for you special function via our contact page.
We look forward to wing able to serve you.
Brindle Coffee.

Contact Us - Safe and secure

To book us at your special function, please fill in your details below and we will respond to your query as soon as possible.

Name:

Company name:

Phone number:

Email address:

Question or comment: ( box )

Brindle Coffee
Harrowvale, Eastmoor, Calvenia
Info@brindlecoffee.com.au
0461 925 274
Operating at your local function or event

Blog
Chatterly and Pictorly integration.

Links

We have a heartfelt passionate and eternal pursuit for exceeding expectations, providing a memorable experience. It follows that we align ourselves with organizations, business's and people who also strive for perfection in what they do, providing great services, products and customer care.

Feel free to contact some of our contacts below who we have found to be above and beyond.

The marrow group - equipment suppliers

http://www.brewtorrik.com.au

Kesh- barista consulting services

https://www.facebook.com/pages/Grand...Kesh/7719302846615098

Reedfinch Swimming Club

http://reedfinch.com.au/

Orvale Baseball Club

www.orvalebrambles.com.au/

Pelling Autos

http://www.pellingautos.com.au

Target Market(s)

Lovers of Coffee at events and functions. Customers wanting coffee catered for at their event of function

Industry/Entity Type

Cafe

Font styles to use
Other font styles liked:
• La Chatte à Maman

Requirements
Must have
• Our logo design
• 5 pages but are open to any suggestions you think would benefit our development. We would also like to have links to our new Chatterly and Pictorly pages on the bottom of each page.
Nice to have
• Your artistic flair and input

```html
<!DOCTYPE html>
<html lang="en">
<head>
<meta charset="utf-8">
<title>Brindle Coffee</title>
<link href="https://fonts.googleapis.com/css2?family=Raleway:wght@400;500;600;700&family=Dancing+Script:wght@700&display=swap" rel="stylesheet">
<style>
:root{
  --brown:#6e2a22;
  --red:#8c2a20;
  --dark:#171210;
  --ink:#2b2522;
  --muted:#8a817c;
  --paper:#ffffff;
  --line:#d9d2ce;
  --footer:#1e1b1a;
}
*{margin:0;padding:0;box-sizing:border-box}
html,body{width:1200px;height:3272px;overflow:hidden}
body{font-family:'Raleway',sans-serif;color:var(--ink);background:var(--paper);position:relative}
.script{font-family:'Dancing Script',cursive;font-weight:700}
section,header,footer{position:absolute;left:0;width:1200px;overflow:hidden}
.center{text-align:center}
.abs{position:absolute;left:0;width:100%}

/* hero */
.hero{top:0;height:610px}
.hero-photo{position:absolute;inset:0;background:radial-gradient(ellipse at 55% 40%,#e9e4dd 0%,#b9a99a 16%,#5a3a26 38%,#2a1a12 68%,#140d09 100%)}
.brand{position:absolute;left:40px;top:22px;width:112px;height:112px;border-radius:50%;background:#1a1210;display:flex;align-items:center;justify-content:center;color:#fff;font-weight:700;font-size:17px;text-align:center;line-height:1.1}
.nav{position:absolute;right:150px;top:56px;display:flex;gap:44px}
.nav a{color:#fff;text-decoration:none;font-size:12px;font-weight:600;letter-spacing:.5px}
.hero-bean{position:absolute;left:572px;top:272px;width:56px;height:56px;border-radius:50%;background:rgba(255,255,255,.88);display:flex;align-items:center;justify-content:center}
.hero h1{position:absolute;top:362px;width:100%;text-align:center;color:#fff;font-size:44px;font-weight:700;text-shadow:0 2px 6px rgba(0,0,0,.5)}
.hero-sub{position:absolute;top:424px;width:100%;text-align:center;color:#f3ece6;font-size:13px}
.wave{position:absolute;left:0;bottom:0}

/* shared */
.sec-title{font-size:36px;font-weight:500;color:var(--ink)}
.sec-title .script{color:var(--red);font-size:42px}
.divider{display:flex;align-items:center;justify-content:center;gap:12px;margin:8px 0}
.divider i{width:60px;height:1px;background:var(--line)}
.divider b{width:12px;height:16px;border-radius:50%;background:var(--brown)}
.kicker{font-size:12px;color:var(--muted)}

/* welcome */
.welcome{top:610px;height:326px}
.welcome .body{width:780px;margin:0 auto 10px;font-size:14px;line-height:1.6;color:#4a423e}
.tagline{color:var(--red);font-size:28px}

/* events */
.events{top:936px;height:484px}
.events-bg{position:absolute;inset:0;background:linear-gradient(180deg,#2a1c16,#120c09)}
.events .sec-title{color:#fff}
.event-photo{position:absolute;left:132px;top:144px;width:248px;height:280px;background:linear-gradient(135deg,#6b4a32,#2a1b12 60%,#8a6446)}
.event-card{position:absolute;left:380px;top:144px;width:692px;height:280px;background:var(--brown);color:#fff;padding:26px 30px;text-align:left}
.event-card h3{font-size:18px;font-weight:600;margin-bottom:14px}
.event-card p{font-size:13px;line-height:1.6;color:#ecdcd6;width:600px}
.event-card .more{position:absolute;left:30px;bottom:24px;font-size:12px;font-weight:700}
.dots{position:absolute;top:446px;width:100%;display:flex;justify-content:center;gap:10px}
.dots span{width:9px;height:9px;border-radius:50%;background:#776660}
.dots span.on{background:#fff}

/* why us */
.why{top:1420px;height:340px}
.features{position:absolute;top:168px;left:150px;width:900px;display:flex;justify-content:space-between}
.feature{width:200px;text-align:center}
.feature svg{display:block;margin:0 auto 14px}
.feature h4{font-size:18px;font-weight:700;margin-bottom:8px}
.feature p{font-size:12px;line-height:1.5;color:var(--muted)}

/* blog */
.blog{top:1760px;height:888px;background:var(--dark);color:#fff}
.blog .sec-title{color:#fff}
.blog .kicker{color:#8d8580}
.timeline{position:absolute;left:599px;top:260px;width:2px;height:610px;background:#5a4a44}
.tl-dot{position:absolute;left:588px;width:24px;height:24px;border-radius:50%;background:var(--red)}
.post{position:absolute;background:var(--brown);text-align:left;padding-bottom:12px}
.post .ph{height:150px;margin:8px;background:linear-gradient(120deg,#3a2a22,#9a8a80 50%,#2b1f19)}
.post h5{font-size:15px;font-weight:600;padding:6px 14px}
.post p{font-size:12px;line-height:1.5;color:#e3d3cd;padding:2px 14px}
.post .meta{display:flex;justify-content:space-between;padding:8px 14px 0;font-size:11px;font-weight:700}
.newsletter{position:absolute;left:632px;top:784px;width:440px;height:44px;display:flex}
.newsletter span{flex:1;background:#fff;color:#999;font-size:12px;padding:14px}
.newsletter b{width:80px;background:var(--red);font-size:12px;display:flex;align-items:center;justify-content:center}

/* booking */
.book{top:2648px;height:212px}
.book .sec-title{font-size:34px}
.book-row{position:absolute;top:150px;left:132px;width:936px;display:flex;gap:18px;text-align:left}
.field{flex:1;height:36px;border-bottom:1px solid var(--line);font-size:12px;color:var(--muted);padding:12px 4px}
.btn{width:170px;height:36px;background:var(--red);color:#fff;font-size:12px;font-weight:700;display:flex;align-items:center;justify-content:center}

/* social */
.social{top:2860px;height:180px;background:var(--brown);color:#fff}
.social-item{position:absolute;top:40px;width:220px;text-align:center;font-size:15px}
.social-item i{display:block;width:56px;height:56px;border-radius:50%;background:#fff;margin:0 auto 16px}

/* footer */
.site-footer{top:3040px;height:232px;background:var(--footer);color:#d6cfcb}
.col{position:absolute;top:28px}
.col h6{font-size:16px;font-weight:600;color:#fff;margin-bottom:10px}
.col .rule{width:300px;height:1px;background:#4a4441;margin-bottom:14px}
.col li{list-style:none;font-size:13px;margin-bottom:10px;display:flex;align-items:center;gap:10px}
.footer-brand{position:absolute;left:920px;top:24px;width:120px;height:120px;border-radius:50%;background:#fff;color:#1a1210;display:flex;align-items:center;justify-content:center;font-size:17px;font-weight:700;text-align:center;line-height:1.1}
.copy{position:absolute;left:880px;top:160px;width:200px;text-align:center;font-size:11px;color:#8d8580}
</style>
</head>
<body>

<header class="hero">
  <div class="hero-photo" role="img" aria-label="Close-up photo of a cup of coffee on a saucer with coffee beans around it"></div>
  <div class="brand">Brindle<br>Coffee</div>
  <nav class="nav"><a href="#">HOME</a><a href="#">ABOUT</a><a href="#">BLOG</a><a href="#">LINKS</a><a href="#">CONTACT</a></nav>
  <div class="hero-bean"><svg width="22" height="30" viewBox="0 0 22 30"><ellipse cx="11" cy="15" rx="10" ry="14" fill="#3a2519"/><path d="M11 2 C6 10 16 20 11 28" stroke="#e9e2da" stroke-width="2" fill="none"/></svg></div>
  <h1>We Have A Passion For Well Made Coffee</h1>
  <p class="hero-sub">Brindle Coffee, a new venture, serving our customers at functions and events, lovingly made coffee from our restored 1976 camper van.</p>
  <svg class="wave" width="1200" height="30" viewBox="0 0 1200 30" preserveAspectRatio="none"><path d="M0 30 V15 Q15 0 30 15 T60 15 T90 15 T120 15 T150 15 T180 15 T210 15 T240 15 T270 15 T300 15 T330 15 T360 15 T390 15 T420 15 T450 15 T480 15 T510 15 T540 15 T570 15 T600 15 T630 15 T660 15 T690 15 T720 15 T750 15 T780 15 T810 15 T840 15 T870 15 T900 15 T930 15 T960 15 T990 15 T1020 15 T1050 15 T1080 15 T1110 15 T1140 15 T1170 15 T1200 15 V30 Z" fill="#fff"/></svg>
</header>

<section class="welcome center">
  <div class="abs" style="top:22px">
    <h2 class="sec-title">Welcome <span style="color:var(--red)">Brindle Coffee</span></h2>
    <div class="divider"><i></i><b></b><i></i></div>
    <p class="kicker">Beautifully made coffee is a pleasure we should all enjoy at least once in our day.</p>
  </div>
  <div class="abs" style="top:142px">
    <p class="body">Served from our restored 1976 camper van we strive to provide you with an experience that will enhance your day. The care we show comes from years of training and experience as a Barista in several countries around the world.</p>
    <p class="body">We trust the joy of our lovingly made coffee and our retro style service will linger.</p>
  </div>
  <p class="abs tagline script" style="top:262px">Serving Great Coffee at an Event or Function Near You</p>
</section>

<section class="events center">
  <div class="events-bg" role="img" aria-label="Dark background photo of roasted coffee beans"></div>
  <h2 class="abs sec-title" style="top:38px">Upcoming <span class="script">Events</span></h2>
  <div class="event-photo" role="img" aria-label="Photo of a barista at work behind an espresso machine at an event"></div>
  <article class="event-card">
    <h3>We trust the joy of our lovingly made coffee</h3>
    <p>Served from our restored 1976 camper van we strive to provide you with an experience that will enhance your day. The care we show comes from years of training and experience as a Barista in several countries around the world that will enhance your day.</p>
    <p style="margin-top:10px">12:00 AM Monday, Spring</p>
    <span class="more">VIEW DETAILS</span>
  </article>
  <div class="dots"><span class="on"></span><span></span><span></span></div>
</section>

<section class="why center">
  <div class="abs" style="top:40px">
    <h2 class="sec-title">Why <span class="script">Us ?</span></h2>
    <div class="divider"><i></i><b></b><i></i></div>
  </div>
  <div class="features">
    <div class="feature">
      <svg width="60" height="50" viewBox="0 0 60 50"><path d="M8 14 H44 V30 Q44 42 26 42 Q8 42 8 30 Z" fill="none" stroke="#8c2a20" stroke-width="3"/><path d="M44 18 Q54 18 54 25 Q54 32 44 32" fill="none" stroke="#8c2a20" stroke-width="3"/><path d="M4 46 H50" stroke="#8c2a20" stroke-width="3"/></svg>
      <h4>BEST COFFEE</h4><p>Served from our restored van we strive to provide an experience that will last.</p>
    </div>
    <div class="feature">
      <svg width="60" height="50" viewBox="0 0 60 50"><circle cx="34" cy="26" r="18" fill="none" stroke="#8c2a20" stroke-width="3"/><path d="M34 16 V26 L42 30" fill="none" stroke="#8c2a20" stroke-width="3"/><path d="M4 20 H14 M2 28 H14 M6 36 H16" stroke="#8c2a20" stroke-width="3"/></svg>
      <h4>FAST SERVICE</h4><p>Served from our restored van we strive to provide an experience that will last.</p>
    </div>
    <div class="feature">
      <svg width="60" height="50" viewBox="0 0 60 50"><rect x="16" y="4" width="30" height="42" fill="none" stroke="#8c2a20" stroke-width="3"/><path d="M22 14 H40 M22 22 H40 M22 30 H40 M22 38 H34" stroke="#8c2a20" stroke-width="2"/></svg>
      <h4>GOOD MENU</h4><p>Served from our restored van we strive to provide an experience that will last.</p>
    </div>
    <div class="feature">
      <svg width="60" height="50" viewBox="0 0 60 50"><path d="M14 38 Q14 12 30 12 Q46 12 46 38 Z" fill="none" stroke="#8c2a20" stroke-width="3"/><path d="M8 40 H52" stroke="#8c2a20" stroke-width="3"/><circle cx="30" cy="8" r="3" fill="#8c2a20"/></svg>
      <h4>JUST GOOD</h4><p>Served from our restored van we strive to provide an experience that will last.</p>
    </div>
  </div>
</section>

<section class="blog center">
  <div class="abs" style="top:50px">
    <h2 class="sec-title">From Our <span class="script">Blog</span></h2>
    <div class="divider"><i></i><b></b><i></i></div>
    <p class="kicker">Beautifully made coffee is a pleasure we should all enjoy each day.</p>
  </div>
  <div class="timeline"></div>
  <div class="tl-dot" style="top:300px"></div>
  <div class="tl-dot" style="top:610px"></div>
  <div class="tl-dot" style="top:794px"></div>

  <article class="post" style="left:136px;top:288px;width:424px">
    <div class="ph" role="img" aria-label="Photo of an espresso machine on a counter"></div>
    <h5>We trust the joy of our lovingly made coffee</h5>
    <p>Served from our restored van we strive to provide you with an experience that will enhance your day. The care we show comes from years of training.</p>
    <div class="meta"><span>August, 2015</span><span>READ MORE</span></div>
  </article>
  <article class="post" style="left:136px;top:632px;width:424px;padding-top:10px">
    <h5>We trust the joy of our lovingly made coffee</h5>
    <p>Served from our restored van we strive to provide you with an experience that will enhance your day. The care we show comes from years of training.</p>
    <div class="meta"><span>August, 2015</span><span>READ MORE</span></div>
  </article>
  <article class="post" style="left:632px;top:264px;width:440px">
    <div class="ph" role="img" aria-label="Photo of a coffee grinder and espresso machine"></div>
    <h5>We trust the joy of our lovingly made coffee</h5>
    <p>Served from our restored van we strive to provide you with an experience that will enhance your day.</p>
    <div class="meta"><span>August, 2015</span><span>READ MORE</span></div>
  </article>
  <article class="post" style="left:632px;top:612px;width:440px;padding-top:10px">
    <h5>We trust the joy of our lovingly made coffee</h5>
    <p>Served from our restored van we strive to provide you with an experience that will enhance your day. The care we show comes from years of training.</p>
    <div class="meta"><span>August, 2015</span><span>READ MORE</span></div>
  </article>
  <div class="newsletter"><span>Your email here</span><b>SEND</b></div>
</section>

<section class="book center">
  <div class="abs" style="top:40px">
    <h2 class="sec-title">Book a Table</h2>
    <div class="divider"><i></i><b></b><i></i></div>
    <p class="kicker">Opening hours from 7AM - 10:00 PM every day we serve</p>
  </div>
  <div class="book-row">
    <div class="field">Date</div><div class="field">Time</div><div class="field">Persons</div><div class="btn">BOOK A TABLE</div>
  </div>
</section>

<section class="social">
  <a class="social-item" style="left:350px"><i></i>Like us on Chatterly</a>
  <a class="social-item" style="left:630px"><i></i>Follow us on Pictorly</a>
</section>

<footer class="site-footer">
  <div class="col" style="left:130px">
    <h6>Links</h6><div class="rule"></div>
    <ul><li>http://www.brewtorrik.com.au</li><li>http://reedfinch.com.au/</li><li>www.orvalebrambles.com.au/</li><li>http://www.pellingautos.com.au</li></ul>
  </div>
  <div class="col" style="left:480px">
    <h6>Contact Us</h6><div class="rule"></div>
    <ul>
      <li><svg width="12" height="16" viewBox="0 0 12 16"><path d="M6 0 A6 6 0 0 1 12 6 C12 10 6 16 6 16 C6 16 0 10 0 6 A6 6 0 0 1 6 0Z" fill="#8c2a20"/><circle cx="6" cy="6" r="2" fill="#1e1b1a"/></svg>Harrowvale, Eastmoor, Calvenia</li>
      <li><svg width="14" height="10" viewBox="0 0 14 10"><rect width="14" height="10" fill="#8c2a20"/><path d="M0 0 L7 6 L14 0" stroke="#1e1b1a" fill="none"/></svg>Info@brindlecoffee.com.au</li>
      <li><svg width="12" height="14" viewBox="0 0 12 14"><path d="M2 0 H5 L6 4 L4 5 Q5 8 8 10 L9 8 L12 9 V12 Q12 14 10 14 Q0 12 0 2 Q0 0 2 0Z" fill="#8c2a20"/></svg>0461 925 274</li>
    </ul>
  </div>
  <div class="footer-brand">Brindle<br>Coffee</div>
  <p class="copy">© All Rights Reserved, 2015 · Brindle Coffee</p>
</footer>

</body>
</html>
```